Plakat-Design für Pfandhaus gesucht
Zielgruppe
Wir sind ein Pfandhaus wir vergeben Pfandkredite gegen Wertgegenstände sowie Juwelier und Goldankauf aber in erster Linie steht das Pfandhaus .
Aufgabenstellung
Ich möchte gerne Plakate Buchen die an Straßen oder Hauswänden befestigt sind. Ca.3,5x3 Meter. Die Botschaft muss kurz und knapp sein da die Leute ja vorbeifahren.

```html
<!DOCTYPE html>
<html lang="de">
<head>
<meta charset="utf-8">
<title>Pfandhaus Barankauf – Plakat</title>
<link href="https://fonts.googleapis.com/css2?family=Bebas+Neue&display=swap" rel="stylesheet">
<style>
  :root {
    --black: #000000;
    --white: #ffffff;
    --gold-light: #f6e27a;
    --gold: #d4af37;
    --gold-dark: #9c7a1c;
    --silver-light: #ffffff;
    --silver: #d9d9d9;
    --silver-dark: #9a9a9a;
    --wall-blue: #4f6f9f;
    --shelf-white: #eeeeee;
    --pig-gold: #c9a13e;
  }
  html, body {
    margin: 0;
    padding: 0;
    overflow: hidden;
    background: var(--black);
  }
  .poster {
    position: relative;
    width: 848px;
    height: 1200px;
    overflow: hidden;
    background: var(--black);
    font-family: "Bebas Neue", "Oswald", sans-serif;
  }
  .web-address {
    position: absolute;
    top: 20px;
    left: 0;
    width: 848px;
    text-align: center;
    color: var(--white);
    font-size: 80px;
    line-height: 1;
    letter-spacing: 1px;
  }
  .gold-rule {
    position: absolute;
    top: 96px;
    left: 0;
    width: 848px;
    height: 27px;
    background: linear-gradient(90deg, var(--gold-dark), var(--gold-light) 30%, var(--gold) 60%, var(--gold-light) 85%, var(--gold-dark));
  }
  .headline {
    position: absolute;
    right: 68px;
    color: var(--white);
    font-size: 140px;
    line-height: 1;
    letter-spacing: 4px;
    margin: 0;
    font-weight: 400;
    text-align: right;
  }
  .headline--first { top: 128px; }
  .headline--second { top: 258px; }
  .shelf-photo {
    position: absolute;
    left: 370px;
    top: 380px;
    width: 478px;
    height: 820px;
    background: linear-gradient(160deg, var(--shelf-white) 0%, var(--wall-blue) 28%, var(--wall-blue) 55%, var(--pig-gold) 85%, var(--shelf-white) 100%);
  }
  .metals {
    position: absolute;
    top: 412px;
    left: 30px;
    font-size: 162px;
    line-height: 1;
    white-space: nowrap;
    letter-spacing: 2px;
  }
  .metals__gold {
    background: linear-gradient(180deg, var(--gold-light), var(--gold) 55%, var(--gold-dark));
    -webkit-background-clip: text;
    background-clip: text;
    color: transparent;
  }
  .metals__and {
    color: var(--white);
    font-size: 92px;
    margin: 0 6px;
  }
  .metals__silver {
    background: linear-gradient(180deg, var(--silver-light), var(--silver) 55%, var(--silver-dark));
    -webkit-background-clip: text;
    background-clip: text;
    color: transparent;
  }
  .cash-badge {
    position: absolute;
    left: 16px;
    top: 580px;
    width: 432px;
    height: 432px;
    border-radius: 50%;
    background: var(--white);
    box-shadow: 8px 4px 0 0 var(--gold);
    text-align: center;
    color: var(--black);
  }
  .cash-badge__text {
    position: absolute;
    left: 0;
    right: 0;
    top: 46px;
  }
  .cash-badge__line {
    display: block;
    line-height: 0.86;
  }
  .cash-badge__line--small { font-size: 110px; }
  .cash-badge__line--large { font-size: 152px; }
</style>
</head>
<body>
<main class="poster">
  <div class="web-address">WWW.PFANDHAUS-LINDENAU.DE</div>
  <div class="gold-rule"></div>

  <div class="shelf-photo" role="img" aria-label="Foto: goldenes Sparschwein in einem weißen Regal in Hausform vor blauer Wand"></div>

  <h1 class="headline headline--first">DAS PFANDHAUS</h1>
  <h2 class="headline headline--second">BARANKAUF</h2>

  <div class="metals">
    <span class="metals__gold">GOLD</span><span class="metals__and">&amp;</span><span class="metals__silver">SILBER</span>
  </div>

  <div class="cash-badge">
    <div class="cash-badge__text">
      <span class="cash-badge__line cash-badge__line--small">SOFORT-</span>
      <span class="cash-badge__line cash-badge__line--small">GELD</span>
      <span class="cash-badge__line cash-badge__line--large">IN BAR</span>
    </div>
  </div>
</main>
</body>
</html>
```